CodeVarnaly.com Redesign

Please read the notes and see the site-map attached.
Updates

We are looking for something highly creative. Please provide your best work. Best of luck and thank you very much for your hard work!

Reason: I am seeing good designs but I am not seeing great designs. I really need a design that is unique and is going to wow me. No one is required to stick to the existing color schemes etc. You are free to use other colors etc. I am seeing a lot of the same colors that are used on the site now.

Target Market(s)

Business and entrepreneurs mainly. People looking to build applications, software or launch web or mobile tech products.

Colors

Designer to choose colors to be used in the design.

Requirements
Must have
• See my attached html file.
Nice to have
Should not have
• No sure

```html
<!DOCTYPE html>
<html lang="en">
<head>
<meta charset="utf-8">
<title>CodeVarnaly.com</title>
<link href="https://fonts.googleapis.com/css2?family=Roboto:wght@300;400;500;700;900&display=swap" rel="stylesheet">
<style>
:root{
  --green:#6cc04a;
  --green-dark:#4f9e2f;
  --navy:#1f3452;
  --navy-deep:#1a2c46;
  --ink:#2b2f36;
  --text:#444a52;
  --muted:#8a9099;
  --line:#d8dbe0;
  --grey-band:#d6d8db;
  --white:#ffffff;
  --orange:#f28a1a;
}
*{box-sizing:border-box;margin:0;padding:0}
html,body{width:1200px;height:2353px;overflow:hidden}
body{position:relative;font-family:"Roboto",Arial,sans-serif;color:var(--text);background:var(--white)}
.abs{position:absolute}

/* header + hero */
.hero{left:0;top:0;width:1200px;height:449px;background:linear-gradient(100deg,#c9d3cc 0%,#e3ebe6 40%,#cfd9d2 70%,#9eaba3 100%);border-top:4px solid var(--green)}
.hero-visual{left:560px;top:110px;width:540px;height:330px;border-radius:12px;background:radial-gradient(ellipse at 60% 60%,#5c6b6f 0%,#8fa19c 35%,rgba(200,212,205,0) 70%)}
.brand{left:172px;top:30px;display:flex;align-items:center;gap:12px}
.brand-mark{width:50px;height:50px;border-radius:50%;background:var(--navy)}
.brand-name{font-size:38px;font-weight:500;color:var(--navy);letter-spacing:-.5px}
.phone{right:148px;top:17px;font-size:18px;color:var(--navy);display:flex;align-items:center;gap:8px}
.top-links{left:752px;top:70px;font-size:14px;color:var(--navy)}
.quote-btn{left:873px;top:63px;width:109px;height:31px;border:2px solid var(--green);border-radius:3px;font-size:14px;color:var(--navy);display:flex;align-items:center;justify-content:center;background:rgba(255,255,255,.5)}
.menu{left:1000px;top:66px;width:26px;height:22px}
.hire-tab{left:1118px;top:59px;width:82px;height:33px;background:var(--white);border-left:4px solid var(--green);font-size:14px;color:var(--navy);display:flex;align-items:center;justify-content:center}
.hero-title{left:172px;top:172px;font-size:35px;font-weight:700;line-height:37px;color:var(--navy);text-transform:uppercase}
.hero-btn{left:172px;top:343px;width:208px;height:33px;background:var(--green);border-radius:3px;color:var(--white);font-size:14px;font-weight:500;display:flex;align-items:center;justify-content:center;gap:10px}
.hero-dots{left:583px;top:421px;display:flex;gap:4px}
.dot{width:9px;height:9px;border-radius:50%;background:var(--white)}
.dot.on{background:#b9c2bc}

/* features */
.feature{width:129px;text-align:center;top:484px}
.feature-box{width:129px;height:94px;border:1px solid var(--line);display:flex;align-items:center;justify-content:center;background:var(--white)}
.feature-label{margin-top:8px;font-size:13px;line-height:16px;color:var(--ink)}

/* section headings */
.section-head{left:172px;width:856px;display:flex;align-items:center;gap:22px}
.section-head::before,.section-head::after{content:"";flex:1;height:5px;background:var(--green)}
.section-head h2{font-size:31px;font-weight:700;color:var(--ink);letter-spacing:.5px;white-space:nowrap}

.lead{left:200px;width:800px;text-align:center;font-size:13px;line-height:17.5px;color:var(--ink)}
.ghost-btn{border:2px solid #9aa0a8;border-radius:3px;font-size:13px;color:var(--ink);display:flex;align-items:center;justify-content:center;background:var(--white)}

/* skills */
.skills{left:0;top:888px;width:1200px;height:432px;background:linear-gradient(90deg,#c4c7cb 0%,#eceef0 35%,#e6e8ea 65%,#c8cbcf 100%)}
.skill{width:180px;text-align:center}
.skill-ring{width:98px;height:98px;margin:0 auto;border-radius:50%;background:var(--white);border:4px solid #5c6470;display:flex;align-items:center;justify-content:center}
.skill-label{margin-top:8px;font-size:15px;color:var(--ink)}
.skills-device{left:569px;top:980px;width:166px;height:296px;border-radius:18px;background:linear-gradient(90deg,#2a2d32 0%,#4b5058 45%,#f0f2f4 46%,#dfe3e8 100%)}
.skills-copy{left:757px;top:1012px;width:270px}
.skills-copy h3{font-size:14px;font-weight:700;color:var(--ink);line-height:17px}
.skills-copy p{margin-top:10px;font-size:12px;line-height:17px;color:#777}

/* video */
.video-frame{left:176px;top:1441px;width:481px;height:255px;border-radius:14px 14px 4px 4px;background:linear-gradient(180deg,#5d6166 0%,#3f4348 100%)}
.video-screen{left:206px;top:1457px;width:421px;height:220px;background:linear-gradient(180deg,#8c9195,#6d7277)}
.video-base{left:176px;top:1677px;width:481px;height:18px;background:linear-gradient(180deg,#cfd2d5,#9ea3a8);border-radius:0 0 40px 40px}
.video-copy{left:666px;top:1460px;width:362px}
.video-copy h3{font-size:17px;font-weight:700;color:var(--ink)}
.video-copy p{margin-top:10px;font-size:12.5px;line-height:18px;color:var(--ink)}
.video-btn{left:670px;top:1615px;width:228px;height:35px;background:var(--green);border:2px solid var(--green-dark);border-radius:3px;color:var(--white);font-size:12.5px;font-weight:500;display:flex;align-items:center;justify-content:center;gap:10px}

/* testimonial */
.avatar{left:537px;top:1827px;width:102px;height:102px;border-radius:50%;border:5px solid var(--green);background:radial-gradient(circle at 50% 40%,#d9b89c,#a87f63 60%,#6e5443)}
.quote-mark{font-size:60px;font-weight:900;color:var(--navy);line-height:1}
.testimonial{left:172px;top:1940px;width:856px;text-align:center;font-size:13px;line-height:18px;color:var(--ink)}
.testimonial b{color:#e7533d;font-weight:700}
.t-dots{left:579px;top:1997px;display:flex;gap:5px}
.t-dots span{width:9px;height:9px;border-radius:50%;background:#cfd3d7}
.t-dots span.on{background:var(--green)}

/* social bar */
.social-bar{left:0;top:2015px;width:1200px;height:47px;background:var(--green)}
.follow{left:176px;top:2025px;font-size:20px;font-weight:700;color:var(--white)}
.social{top:2020px;display:flex;align-items:center;gap:12px;font-size:13px;color:var(--white)}
.social i{width:38px;height:38px;border-radius:50%;background:var(--white);display:block}

/* footer */
.footer{left:0;top:2062px;width:1200px;height:291px;background:var(--navy)}
.foot-col h4{font-size:18px;font-weight:500;color:var(--white);padding-bottom:7px;border-bottom:1px solid #3c5070}
.foot-links{list-style:none;margin-top:6px}
.foot-links li{font-size:12.5px;color:var(--white);height:26.5px;line-height:26px;border-bottom:1px solid #33486a}
.foot-links li::before{content:"›";margin-right:6px}
.contact-row{display:flex;gap:14px;font-size:12.5px;color:var(--white);line-height:16px;margin-top:20px}
.newsletter p{margin-top:14px;font-size:12.5px;line-height:16px;color:var(--white)}
.email-field{margin-top:12px;width:251px;height:31px;background:var(--white);font-size:12px;color:#b5b9bf;padding:8px 12px}
.submit{margin:20px 0 0 185px;width:66px;height:35px;border:1px solid var(--white);border-radius:4px;color:var(--white);font-size:14px;display:flex;align-items:center;justify-content:center}

/* chat widget */
.chat{left:1010px;top:1974px;width:170px;height:94px}
.chat-bubble{width:170px;height:60px;background:var(--orange);border-radius:12px;padding:8px 12px;color:var(--white)}
.chat-bubble strong{font-size:16px;display:block}
.chat-bubble span{font-size:10px}
.chat-badge{margin-top:4px;width:164px;height:26px;background:#eef0f2;border:1px solid #c6c9cd;font-size:11px;color:var(--ink);display:flex;align-items:center;gap:6px;padding:0 8px}
.chat-badge i{width:10px;height:10px;border-radius:50%;background:#9aa0a6;display:block}
</style>
</head>
<body>

<header class="hero abs">
</header>
<div class="hero-visual abs" role="img" aria-label="Smartphone with colourful app icons flying out of its screen"></div>

<div class="brand abs"><span class="brand-mark"></span><span class="brand-name">codevarnaly</span></div>
<div class="phone abs">
  <svg width="22" height="22" viewBox="0 0 24 24"><path d="M6.6 10.8a15 15 0 0 0 6.6 6.6l2.2-2.2c.3-.3.7-.4 1-.2 1.1.4 2.3.6 3.6.6.6 0 1 .4 1 1V20c0 .6-.4 1-1 1A17 17 0 0 1 3 4c0-.6.4-1 1-1h3.5c.6 0 1 .4 1 1 0 1.3.2 2.5.6 3.6.1.3 0 .7-.2 1z" fill="#6cc04a"/></svg>
  877 555 0142
</div>
<div class="top-links abs">Login &nbsp;|&nbsp; Register</div>
<div class="quote-btn abs">Get a Quote</div>
<svg class="menu abs" viewBox="0 0 26 22"><rect y="1" width="26" height="4" fill="#1f3452"/><rect y="9" width="26" height="4" fill="#1f3452"/><rect y="17" width="26" height="4" fill="#1f3452"/></svg>
<div class="hire-tab abs">Hire Us !</div>

<h1 class="hero-title abs">Providing better<br>solutions<br>for your online<br>presence</h1>
<div class="hero-btn abs">Click here for more detail
  <svg width="16" height="16" viewBox="0 0 16 16"><circle cx="8" cy="8" r="8" fill="#fff"/><path d="M6 4.5 9.5 8 6 11.5" stroke="#6cc04a" stroke-width="2" fill="none"/></svg>
</div>
<div class="hero-dots abs"><span class="dot on"></span><span class="dot"></span></div>

<!-- feature row -->
<div class="feature abs" style="left:175px">
  <div class="feature-box"><svg width="60" height="54" viewBox="0 0 60 54"><rect x="3" y="3" width="54" height="40" rx="3" fill="none" stroke="#2aa3d8" stroke-width="4"/><circle cx="30" cy="23" r="9" fill="none" stroke="#2aa3d8" stroke-width="3"/><rect x="22" y="45" width="16" height="6" fill="#2aa3d8"/></svg></div>
  <div class="feature-label">Intuitive<br>UI</div>
</div>
<div class="feature abs" style="left:320px">
  <div class="feature-box"><svg width="56" height="60" viewBox="0 0 56 60"><rect x="12" y="6" width="32" height="24" rx="4" fill="#5bb030"/><rect x="16" y="32" width="24" height="20" fill="#5bb030"/><rect x="2" y="34" width="10" height="14" fill="#5bb030"/><rect x="44" y="34" width="10" height="14" fill="#5bb030"/><circle cx="22" cy="17" r="4" fill="#fff"/><circle cx="34" cy="17" r="4" fill="#fff"/></svg></div>
  <div class="feature-label">Robust<br>Engineering</div>
</div>
<div class="feature abs" style="left:463px">
  <div class="feature-box"><svg width="56" height="56" viewBox="0 0 56 56"><path d="M6 8h20l24 24-18 18L8 26z" fill="#2b3a55"/><circle cx="16" cy="17" r="4" fill="#fff"/></svg></div>
  <div class="feature-label">Unified Aesthetic<br>Designs</div>
</div>
<div class="feature abs" style="left:606px">
  <div class="feature-box"><svg width="66" height="54" viewBox="0 0 66 54"><rect x="14" y="4" width="48" height="32" rx="2" fill="none" stroke="#f0902a" stroke-width="4"/><rect x="2" y="18" width="24" height="32" rx="2" fill="#fff" stroke="#f0902a" stroke-width="4"/><rect x="32" y="40" width="20" height="5" fill="#f0902a"/></svg></div>
  <div class="feature-label">Multiple Device<br>Compatibility</div>
</div>
<div class="feature abs" style="left:751px">
  <div class="feature-box"><svg width="60" height="58" viewBox="0 0 60 58"><g fill="#8c6fd8"><ellipse cx="38" cy="12" rx="18" ry="7"/><rect x="20" y="12" width="36" height="30"/><ellipse cx="38" cy="42" rx="18" ry="7"/><ellipse cx="20" cy="30" rx="16" ry="6"/><rect x="4" y="30" width="32" height="18"/><ellipse cx="20" cy="48" rx="16" ry="6"/></g><g stroke="#fff" stroke-width="1.5" fill="none"><path d="M20 22h36M20 32h36M4 40h32"/></g></svg></div>
  <div class="feature-label" style="font-size:12px">Cost Effective<br>solution</div>
</div>
<div class="feature abs" style="left:894px">
  <div class="feature-box"><svg width="36" height="60" viewBox="0 0 36 60"><rect x="2" y="2" width="32" height="56" rx="5" fill="#e32222"/><rect x="7" y="10" width="22" height="28" fill="#fff"/><circle cx="18" cy="48" r="4" fill="#fff"/></svg></div>
  <div class="feature-label" style="font-size:12px">Transparent<br>Communication</div>
</div>

<!-- welcome -->
<div class="section-head abs" style="top:676px"><h2>WELCOME TO CODEVARNALY</h2></div>
<p class="lead abs" style="top:729px">Praesent ipsum nisi, dapibus tempus sodales quis, vehicula suscipit nulla. Etiam dictum lacus non lacus pharetra viverra. Donec dignissim sed lorem a pulvinar. Praesent varius odio pellentesque vulputate mattis. Morbi nec adipiscing dui. Nam faucibus placerat odio, a rutrum urna venenatis id. In in laoreet urna.</p>
<div class="ghost-btn abs" style="left:553px;top:808px;width:98px;height:33px">View more »</div>

<!-- skills -->
<section class="skills abs"></section>
<div class="section-head abs" style="top:917px"><h2>OUR SKILLS</h2></div>

<div class="skill abs" style="left:171px;top:992px">
  <div class="skill-ring"><svg width="52" height="52" viewBox="0 0 52 52" fill="none" stroke="#1f3452" stroke-width="3"><path d="M8 40 24 24M44 40 28 24"/><path d="M6 12l10 10M46 12 36 22"/><path d="M12 44h28"/></svg></div>
  <div class="skill-label">Web Development</div>
</div>
<div class="skill abs" style="left:343px;top:992px">
  <div class="skill-ring"><svg width="52" height="52" viewBox="0 0 52 52" fill="none" stroke="#1f3452" stroke-width="3"><path d="M8 44 22 30l8 6 14-20"/><path d="M36 16h8v8"/></svg></div>
  <div class="skill-label">SEO</div>
</div>
<div class="skill abs" style="left:171px;top:1145px">
  <div class="skill-ring"><svg width="52" height="52" viewBox="0 0 52 52" fill="none" stroke="#1f3452" stroke-width="3"><path d="M10 42 38 14l4 4-28 28H10z"/><path d="M14 10l28 28"/></svg></div>
  <div class="skill-label">Graphic Design</div>
</div>
<div class="skill abs" style="left:343px;top:1145px">
  <div class="skill-ring"><svg width="52" height="52" viewBox="0 0 52 52" fill="none" stroke="#1f3452" stroke-width="3"><rect x="8" y="14" width="24" height="26" rx="2"/><path d="M24 27h20M36 19l8 8-8 8"/></svg></div>
  <div class="skill-label">Outsourcing</div>
</div>

<div class="skills-device abs" role="img" aria-label="Two smartphones showing a mobile version of the website"></div>
<div class="skills-copy abs">
  <h3>venenatis eu purus sed, pretium tincidunt lectus</h3>
  <p>Curabitur varius dui ac sapien suscipit bibendum. Suspendisse pulvinar neque quis tincidunt iaculis. Nulla ante mi, euismod placerat adipiscing ac, hendrerit ac nunc. Vivamus in erat massa. Etiam sodales imperdiet urna sit amet sodales. Suspendisse porttitor facilisis leo,</p>
  <p>in imperdiet libero condimentum sed. Maecenas ac vulputate ante. Morbi in nibh non</p>
</div>
<div class="ghost-btn abs" style="left:939px;top:1241px;width:86px;height:31px;border-color:var(--green);background:transparent">View more »</div>

<!-- video -->
<div class="section-head abs" style="top:1364px"><h2>OUR VIDEO</h2></div>
<div class="video-frame abs"></div>
<div class="video-screen abs" role="img" aria-label="Video preview of the website homepage shown on a laptop screen"></div>
<svg class="abs" style="left:396px;top:1540px" width="48" height="54" viewBox="0 0 48 54"><path d="M4 2 46 27 4 52z" fill="#fff" opacity=".9"/></svg>
<div class="video-base abs"></div>
<div class="video-copy abs">
  <h3>Donec dignissim sed lorem a pulvinar.</h3>
  <p>Sed sed venenatis lorem. Mauris placerat semper suscipit. In dictum euismod feugiat. Phasellus vitae sapien ut urna hendrerit dictum. Interdum et malesuada fames ac ante ipsum primis in faucibus. Cras ultricies odio et nulla pharetra, vitae consectetur mi venenatis. Sed vehicula ligula vitae metus vulputate, vitae posuere lectus interdum.</p>
</div>
<div class="video-btn abs">CLICK HERE FOR MORE VIDEOS
  <svg width="16" height="16" viewBox="0 0 16 16"><circle cx="8" cy="8" r="8" fill="#fff"/><path d="M6 4.5 9.5 8 6 11.5" stroke="#6cc04a" stroke-width="2" fill="none"/></svg>
</div>

<!-- testimonial -->
<div class="section-head abs" style="top:1766px"><h2>WHAT CLIENT SAYS</h2></div>
<div class="quote-mark abs" style="left:494px;top:1858px">“</div>
<div class="avatar abs" role="img" aria-label="Portrait photo of the client"></div>
<div class="quote-mark abs" style="left:652px;top:1858px">”</div>
<p class="testimonial abs">Lorem ipsum dolor sit amet, consectetur adipisicing elit. Facilis minus pariatur eligendi sunt doloremque vitae reiciendis tempore voluptatibus quis architecto suscipit magnam. Lorem ipsum dolor sit amet, consectetur adipisicing elit. Facilis minus pariatur eligendi. - <b>Rina Calloway</b></p>
<div class="t-dots abs"><span class="on"></span><span></span><span></span></div>

<!-- social -->
<div class="social-bar abs"></div>
<div class="follow abs">Follow us at:</div>
<div class="social abs" style="left:336px"><i></i>FaceSpace</div>
<div class="social abs" style="left:517px"><i></i>Chirper</div>
<div class="social abs" style="left:697px"><i></i>LinkHub</div>
<div class="social abs" style="left:895px"><i></i>PlusCircle</div>

<!-- footer -->
<footer class="footer abs"></footer>
<div class="foot-col abs" style="left:172px;top:2142px;width:244px">
  <h4>Site Info</h4>
  <ul class="foot-links">
    <li>Home</li><li>Who We Are</li><li>What We Do</li><li>Our Recent Work</li><li>Blog</li><li>Contact Us</li>
  </ul>
</div>
<div class="foot-col abs" style="left:474px;top:2142px;width:256px">
  <h4>Contact Us</h4>
  <div class="contact-row"><svg width="14" height="14" viewBox="0 0 14 14"><path d="M7 1 1 7h2v6h3V9h2v4h3V7h2z" fill="#fff"/></svg><span>6360 Phasellus congue metus<br>purus, in porttitor nisi suscipit ut</span></div>
  <div class="contact-row"><svg width="14" height="14" viewBox="0 0 24 24"><path d="M6.6 10.8a15 15 0 0 0 6.6 6.6l2.2-2.2c.3-.3.7-.4 1-.2 1.1.4 2.3.6 3.6.6.6 0 1 .4 1 1V20c0 .6-.4 1-1 1A17 17 0 0 1 3 4c0-.6.4-1 1-1h3.5c.6 0 1 .4 1 1 0 1.3.2 2.5.6 3.6.1.3 0 .7-.2 1z" fill="#fff"/></svg><span>788-555-0193</span></div>
  <div class="contact-row"><svg width="14" height="14" viewBox="0 0 14 14"><rect x="1" y="3" width="12" height="8" fill="#fff"/><path d="M1 3l6 5 6-5" stroke="#1f3452" fill="none"/></svg><span>info@codevarnaly.com</span></div>
</div>
<div class="foot-col newsletter abs" style="left:767px;top:2142px;width:260px">
  <h4>Subscribe Newsletter</h4>
  <p>Enter your email address to reiceive all news from our awesome website</p>
  <div class="email-field">enter email address</div>
  <div class="submit">Submit</div>
</div>

<!-- chat widget -->
<div class="chat abs">
  <div class="chat-bubble"><strong>Questions?</strong><span>Click here to chat with us!</span></div>
  <div class="chat-badge"><i></i>Offline - Leave a message</div>
</div>

</body>
</html>
```